Letter Head Design

I need a letter head design based on my company logo that I attached.
Include phone number: (403)582-4316
Address: 347 14th Avenue NE, Calgary, Alberta, Canada, T3K 4R8

Industry/Entity Type

It Company

```html
<!DOCTYPE html>
<html lang="en">
<head>
<meta charset="utf-8">
<title>Northvale Interiors Corp. – Letterhead</title>
<link href="https://fonts.googleapis.com/css2?family=Open+Sans:wght@400;600&family=EB+Garamond:wght@400;500&family=Roboto+Condensed:wght@400&display=swap" rel="stylesheet">
<style>
  :root {
    --backdrop: #e4e4e4;
    --paper: #ffffff;
    --brand-blue: #1f5fae;
    --brand-green: #4ca843;
    --ink: #1a1a1a;
    --body-ink: #555555;
    --muted: #666666;
    --signature-tone: #ececec;
  }
  * { box-sizing: border-box; margin: 0; padding: 0; }
  html, body {
    width: 1158px; height: 1200px; overflow: hidden;
    background: var(--backdrop);
  }
  .letterhead {
    position: absolute; left: 169px; top: 20px;
    width: 820px; height: 1160px;
    background: var(--paper);
    box-shadow: 0 4px 14px rgba(0,0,0,0.18);
  }
  .edge-rule { position: absolute; left: 0; width: 100%; height: 4px; }
  .edge-rule--top { top: 0; background: var(--brand-blue); }
  .edge-rule--bottom { bottom: 0; background: var(--brand-green); }

  .brand {
    position: absolute; top: 180px; left: 0; width: 100%;
    text-align: center;
    font-family: "Open Sans", sans-serif; font-weight: 600;
    font-size: 36px; line-height: 44px; color: var(--brand-blue);
    letter-spacing: -0.5px;
  }

  .recipient {
    position: absolute; top: 312px; left: 0; width: 100%;
    text-align: center; font-family: "EB Garamond", serif; color: var(--ink);
  }
  .recipient__name { font-size: 25px; font-weight: 500; line-height: 32px; }
  .recipient__role { font-size: 18px; line-height: 26px; }

  .letter-body {
    position: absolute; top: 414px; left: 92px; width: 632px;
    font-family: "Open Sans", sans-serif; color: var(--body-ink);
  }
  .letter-body__heading { font-size: 11px; color: var(--muted); margin-bottom: 20px; }
  .letter-body p {
    font-size: 14px; line-height: 21.4px; text-align: justify;
    margin-bottom: 27px;
  }

  .signature {
    position: absolute; top: 990px; left: 538px;
    width: 176px; height: 50px; background: var(--signature-tone);
    border-radius: 4px;
  }

  .contact-line {
    position: absolute; top: 1116px; left: 48px; right: 32px;
    display: flex; justify-content: space-between;
    font-family: "Roboto Condensed", sans-serif; font-size: 21px; color: var(--ink);
  }
</style>
</head>
<body>
  <main class="letterhead">
    <div class="edge-rule edge-rule--top"></div>

    <header class="brand">Northvale Interiors Corp.</header>

    <section class="recipient">
      <div class="recipient__name">Mr. LOREM IPSUM</div>
      <div class="recipient__role">Designation, Company Name</div>
    </section>

    <article class="letter-body">
      <div class="letter-body__heading">LOREM IPSUM DUMMY TEXT</div>
      <p>Lorem Ipsum is simply dummy text of the printing and typesetting industry. Lorem Ipsum has been the industry's standard dummy text ever since the 1500s, when an unknown printer took a galley of typeand scrambled it to make a type specimen book. It has survived not only ve centuries, but also the leap into electronic typesetting, remaining essentially unchanged. It was popularised in the 1960s with the release of Letraset sheets containing Lorem Ipsum passages, and more recently with desktop publishing software like Aldus PageMaker including versions of Lorem Ipsum.</p>
      <p>Lorem Ipsum is simply dummy text of the printing and typesetting industry. Lorem Ipsum has been the industry's standard dummy text ever since the 1500s, when an unknown printer took a galley of type and scrambled it to make a type specimen book. It has survived not only _ve centuries, but also the leap into electronic typesetting, remaining essentially unchanged. It was popularised in the 1960s with the release of Letraset sheets containing Lorem Ipsum passages, and more recently with desktop publishing software like Aldus PageMaker including versions of Lorem Ipsum.</p>
      <p>Lorem Ipsum is simply dummy text of the printing and typesetting industry. Lorem Ipsum has been the industry's standard dummy text ever since the 1500s, when an unknown printer took a galley of type and scrambled it to make a type specimen book. It has survived not only _ve centuries, but also the leap into electronic typesetting, remaining essentially unchanged. It was popularised in the 1960s with the release of Letraset sheets containing Lorem Ipsum passages, and more recently with desktop publishing software like Aldus PageMaker including versions of Lorem Ipsum.</p>
    </article>

    <div class="signature" role="img" aria-label="Handwritten signature of the sender"></div>

    <footer class="contact-line">
      <span class="contact-line__phone">(403)582-4316</span>
      <span class="contact-line__address">347 14th Avenue NE, Calgary, Alberta, Canada, T3K 4R8</span>
    </footer>

    <div class="edge-rule edge-rule--bottom"></div>
  </main>
</body>
</html>
```